I have just launched a labour hire company and lookingfor a fresh vibrant website design

I need a landing page, a description of our services and capability, as well as an enquiries link, and register candidates link. My company is called Kestrel9 recruitment and we supply labourers, excavator operators, and machine operators to the Civil and railway industries. I would like to stick to our logo theme and colours of Bright green, although I want a brighter green please than what I have. I have attached Images I like as well plaese. I do need a much bigger website eventually.

```html
<!DOCTYPE html>
<html lang="en">
<head>
<meta charset="utf-8">
<title>Kestrel9 Recruitment</title>
<link href="https://fonts.googleapis.com/css2?family=Michroma&family=Roboto:wght@400;500;700&display=swap" rel="stylesheet">
<style>
:root{
  --green:#17b320;
  --green-band:#0fa82c;
  --green-pale:#eef8ef;
  --ink:#1a1a1a;
  --muted:#777;
  --white:#fff;
  --footer:#121212;
  --grey-bg:#f5f5f5;
  --star:#f5a623;
}
*{box-sizing:border-box;margin:0;padding:0}
html,body{width:1200px;height:4119px;overflow:hidden}
body{position:relative;font-family:"Roboto",Arial,sans-serif;color:var(--ink);background:var(--white)}
.abs{position:absolute}
.display{font-family:"Michroma",sans-serif;font-weight:400;text-transform:uppercase}
.mark{display:inline-block;width:20px;height:20px;background:var(--green);vertical-align:middle;margin-right:16px}

/* header */
.site-header{left:0;top:0;width:1200px;height:130px;background:var(--white)}
.brand{left:110px;top:44px;display:flex;align-items:center;gap:12px;font-family:"Michroma",sans-serif;font-size:21px;color:var(--ink)}
.brand .sq{width:26px;height:26px;background:var(--green)}
.nav{left:438px;top:59px;display:flex;gap:22px;font-size:14px;font-weight:700}
.nav a{color:var(--ink);text-decoration:none}
.nav a.active{color:var(--green)}
.call{left:855px;top:42px;display:flex;align-items:center;gap:18px}
.call .ring{width:50px;height:50px;border-radius:50%;background:var(--green);display:flex;align-items:center;justify-content:center;box-shadow:0 0 0 4px #d9f2da}
.call small{display:block;font-size:11px;color:var(--ink)}
.call strong{display:block;font-size:22px;color:var(--green);font-weight:700;margin-top:2px}

/* hero */
.hero{left:0;top:130px;width:1200px;height:617px;background:linear-gradient(160deg,#4a4036 0%,#b4783a 35%,#d99a4a 55%,#8a5a2c 80%,#3a2a1c 100%)}
.hero h1{left:110px;top:180px;font-size:34px;line-height:47px;color:var(--white)}
.hero p{left:111px;top:286px;font-size:19px;line-height:32px;color:var(--white)}
.btn{display:inline-block;background:var(--green);color:var(--white);font-weight:700;font-size:13px;text-transform:uppercase;box-shadow:5px 5px 0 -1px var(--white),5px 5px 0 1px var(--ink)}
.hero .btn{left:112px;top:376px;width:140px;height:48px;line-height:48px;text-align:center;box-shadow:5px 5px 0 -1px transparent,5px 5px 0 1px var(--white)}
.dots{display:flex;gap:12px}
.dots i{width:11px;height:11px;border-radius:50%;border:1.5px solid var(--white)}
.dots i.on{background:var(--white)}
.hero .dots{left:559px;top:576px}

/* about */
.about-photo{border:6px solid var(--white)}
.about h2{left:676px;top:912px;font-size:35px}
.about p{left:675px;top:978px;width:414px;font-size:13px;line-height:25.7px;color:var(--muted);text-align:justify}
.about .btn{left:675px;top:1220px;width:124px;height:46px;line-height:46px;text-align:center}

/* services */
.services{left:0;top:1435px;width:1200px;height:592px;background:var(--green-pale)}
.sec-title{left:0;width:1200px;text-align:center;font-size:35px}
.svc{top:155px;width:300px;height:360px;background:var(--white);padding:6px;box-shadow:0 2px 10px rgba(0,0,0,.08)}
.svc .ph{width:288px;height:348px;position:relative}
.svc span{position:absolute;left:0;right:0;bottom:30px;text-align:center;color:var(--white);font-weight:700;font-size:16px;text-transform:uppercase}

/* process */
.process{left:0;top:2027px;width:1200px;height:598px;background:var(--green-band)}
.step{top:154px;width:228px;height:337px;border:2px solid var(--white);color:var(--white);text-align:center;padding:28px 14px 0}
.step.lit{background:var(--white);color:var(--ink)}
.step h3{font-size:15px;line-height:24px;margin-top:14px;text-transform:uppercase}
.step p{font-size:12.5px;line-height:23px;margin-top:6px}
.step.lit p{color:var(--muted)}
.step a{display:block;margin-top:8px;font-size:13.5px;font-weight:700;color:inherit;text-decoration:underline}
.step.lit a{color:var(--green)}
.step svg{display:block;margin:0 auto}

/* testimonials */
.quote{top:2828px;width:306px;height:277px;background:var(--white);box-shadow:0 3px 14px rgba(0,0,0,.1);padding:22px 24px}
.stars{color:var(--star);font-size:14px;letter-spacing:1px}
.quote p{margin-top:10px;font-size:14.5px;line-height:25.5px;color:var(--muted);text-align:justify}
.quote hr{border:0;border-top:1px solid #e2e2e2;margin:16px 0 12px}
.who{display:flex;align-items:center;gap:16px}
.avatar{width:56px;height:56px;border-radius:50%;background:linear-gradient(#cfc6bc,#8d7f72)}
.who b{display:block;color:var(--green);font-size:14px}
.who small{font-size:11px}
.arrow{top:2947px;width:36px;height:36px;border-radius:50%;display:flex;align-items:center;justify-content:center}

/* contact */
.contact{left:0;top:3245px;width:1200px;height:463px;background:var(--grey-bg)}
.field{background:var(--white);box-shadow:0 2px 8px rgba(0,0,0,.08);font-size:13px;color:#555;padding:0 17px;line-height:47px}
.send{left:520px;top:335px;width:160px;height:47px;line-height:47px;text-align:center;background:var(--green);color:var(--white);font-weight:700;font-size:14px}

/* footer */
.footer{left:0;top:3708px;width:1200px;height:411px;background:var(--footer);color:var(--white)}
.footer .brand{left:110px;top:172px;color:var(--white);font-size:22px}
.fcol h4{font-size:15px;font-weight:700;text-transform:uppercase;padding-bottom:14px;border-bottom:2px solid var(--green)}
.frow{display:flex;gap:18px;align-items:center;margin-top:18px;font-size:13px;line-height:23px}
.ico{flex:none;width:36px;height:36px;border-radius:50%;background:var(--white);display:flex;align-items:center;justify-content:center}
.links li{list-style:none;font-size:13px;margin-top:14px}
.copy{left:0;top:337px;width:1200px;border-top:1px solid #333;padding-top:22px;text-align:center;font-size:13px}
</style>
</head>
<body>

<header class="abs site-header">
  <div class="abs brand"><span class="sq"></span>Kestrel9 Recruitment</div>
  <nav class="abs nav"><a class="active">HOME</a><a>ABOUT</a><a>SERVICES</a><a>BLOG</a><a>CONTACT</a></nav>
  <div class="abs call">
    <div class="ring"><svg width="22" height="22" viewBox="0 0 24 24"><path fill="#fff" d="M6.6 10.8a15 15 0 0 0 6.6 6.6l2.2-2.2c.3-.3.7-.4 1-.2 1.1.4 2.3.6 3.6.6.6 0 1 .4 1 1V20c0 .6-.4 1-1 1A17 17 0 0 1 3 4c0-.6.4-1 1-1h3.5c.6 0 1 .4 1 1 0 1.3.2 2.5.6 3.6.1.3 0 .7-.2 1z"/></svg></div>
    <div><small>Call Us Today!</small><strong>+1 300 555 018</strong></div>
  </div>
</header>

<section class="abs hero" role="img" aria-label="Yellow excavator digging soil at sunset under a cloudy sky">
  <h1 class="abs display">NSW Civil &amp; Rail<br>Labour Specialists</h1>
  <p class="abs">Kestrel9 Recruitment is a NSW labour hire agency<br>specialising in the civil sector.</p>
  <a class="abs btn">Get Started</a>
  <div class="abs dots"><i></i><i class="on"></i><i></i><i></i></div>
</section>

<section class="about">
  <div class="abs about-photo" style="left:297px;top:881px;width:335px;height:245px;background:linear-gradient(#f0a020,#c8641a 60%,#1c1c1c);border-color:transparent" role="img" aria-label="Excavator silhouette against an orange sunset"></div>
  <div class="abs about-photo" style="left:105px;top:999px;width:305px;height:207px;background:linear-gradient(100deg,#e2672d,#c9c3bc 60%,#8d8a86)" role="img" aria-label="Rail workers in orange hi-vis on a track"></div>
  <div class="abs about-photo" style="left:297px;top:1094px;width:279px;height:214px;background:linear-gradient(#6b5540,#c98f3c 55%,#4a3a2a)" role="img" aria-label="Excavator working inside a lit tunnel"></div>
  <h2 class="abs display"><span class="mark"></span>About Us</h2>
  <p class="abs">Kestrel9 Recruitment is a NSW labour hire agency specialising in the civil sector. With a strong track record of providing skilled and reliable workers to the civil and rail construction industry, we have established ourselves as a trusted partner for companies seeking efficient and cost-effective staffing solutions. Our team of experienced professionals is dedicated to meeting the specific needs of our clients, ensuring seamless project execution and successful outcomes.</p>
  <a class="abs btn">Read More</a>
</section>

<section class="abs services">
  <h2 class="abs display sec-title" style="top:70px"><span class="mark"></span>Our Services</h2>
  <div class="abs svc" style="left:111px"><div class="ph" role="img" aria-label="Workers in hi-vis vests reviewing plans beside a hard hat" style="background:linear-gradient(#8a9a70,#c9b98a 50%,#5a5240)"><span>Labourers</span></div></div>
  <div class="abs svc" style="left:451px"><div class="ph" role="img" aria-label="Excavator operator in hard hat beside his machine" style="background:linear-gradient(#a9aaa8,#7a7560 50%,#3e3a32)"><span>Excavator Operators</span></div></div>
  <div class="abs svc" style="left:789px"><div class="ph" role="img" aria-label="Technician operating an industrial machine" style="background:linear-gradient(#6f7f8c,#3d4650 60%,#22282e)"><span>Machine Operators</span></div></div>
</section>

<section class="abs process">
  <h2 class="abs display sec-title" style="top:72px;color:var(--white)"><span class="mark" style="background:var(--white)"></span>The Process</h2>
  <div class="abs step" style="left:111px">
    <svg width="54" height="54" viewBox="0 0 54 54" fill="none" stroke="#fff" stroke-width="2"><circle cx="27" cy="27" r="22" stroke-dasharray="5 3"/><circle cx="27" cy="27" r="13"/><circle cx="27" cy="27" r="5"/></svg>
    <h3>Rigorous<br>Selection Process</h3>
    <p>Kestrel9 Recruitment employs a meticulous selection process to identify and choose the most qualified and experienced civil labourers and operators.</p>
    <a>READ MORE</a>
  </div>
  <div class="abs step" style="left:361px">
    <svg width="54" height="54" viewBox="0 0 54 54" fill="none" stroke="#fff" stroke-width="2"><rect x="8" y="5" width="28" height="40" rx="2"/><path d="M14 16h16M14 24h10M14 32h8"/><circle cx="36" cy="36" r="8"/><path d="M42 42l7 7"/></svg>
    <h3>Compliance<br>Verification</h3>
    <p>The agency places a strong emphasis on compliance with industry regulations and standards. They verify that all candidates possess</p>
    <a>READ MORE</a>
  </div>
  <div class="abs step lit" style="left:611px">
    <svg width="54" height="54" viewBox="0 0 54 54" fill="none" stroke="#17b320" stroke-width="2"><circle cx="30" cy="16" r="10"/><path d="M26 16l3 3 6-6"/><path d="M6 48c4-10 10-16 18-18l6 6"/><path d="M14 40l6 6"/></svg>
    <h3>Reference<br>Checking</h3>
    <p>Kestrel9 Recruitment understands the importance of reliable references. They conduct thorough reference checks on all candidates to validate</p>
    <a>READ MORE</a>
  </div>
  <div class="abs step" style="left:861px">
    <svg width="54" height="54" viewBox="0 0 54 54" fill="none" stroke="#fff" stroke-width="2"><circle cx="27" cy="27" r="22" stroke-dasharray="5 3"/><circle cx="27" cy="22" r="6"/><path d="M16 38c2-6 6-9 11-9s9 3 11 9"/></svg>
    <h3>Skill<br>Assessment</h3>
    <p>The agency assesses the technical competencies and skill levels of each candidate during the selection process. This includes evaluating</p>
    <a>READ MORE</a>
  </div>
  <div class="abs dots" style="left:583px;top:522px"><i class="on"></i><i></i></div>
</section>

<section class="testimonials">
  <h2 class="abs display sec-title" style="top:2745px"><span class="mark"></span>Testimonials</h2>
  <div class="abs arrow" style="left:34px"><svg width="14" height="14" viewBox="0 0 14 14"><path d="M9 2L4 7l5 5" fill="none" stroke="#1a1a1a" stroke-width="2"/></svg></div>
  <div class="abs arrow" style="left:1129px;background:var(--green)"><svg width="14" height="14" viewBox="0 0 14 14"><path d="M5 2l5 5-5 5" fill="none" stroke="#fff" stroke-width="2"/></svg></div>
  <div class="abs quote" style="left:111px"><div class="stars">★★★★★</div><p>Lorem ipsum dolor sit amet, consectetur adipiscing elit, sed do eiusmod tempor incididunt ut labore et dolore magna aliqua.</p><hr><div class="who"><div class="avatar" role="img" aria-label="Client portrait"></div><div><b>JOHN SMITH</b><small>Australia</small></div></div></div>
  <div class="abs quote" style="left:447px"><div class="stars">★★★★★</div><p>Lorem ipsum dolor sit amet, consectetur adipiscing elit, sed do eiusmod tempor incididunt ut labore et dolore magna aliqua.</p><hr><div class="who"><div class="avatar" role="img" aria-label="Client portrait"></div><div><b>JOHN SMITH</b><small>Australia</small></div></div></div>
  <div class="abs quote" style="left:783px"><div class="stars">★★★★★</div><p>Lorem ipsum dolor sit amet, consectetur adipiscing elit, sed do eiusmod tempor incididunt ut labore et dolore magna aliqua.</p><hr><div class="who"><div class="avatar" role="img" aria-label="Client portrait"></div><div><b>JOHN SMITH</b><small>Australia</small></div></div></div>
</section>

<section class="abs contact">
  <h2 class="abs display sec-title" style="top:80px"><span class="mark"></span>Contact Us</h2>
  <div class="abs field" style="left:165px;top:163px;width:283px;height:47px">Full Name</div>
  <div class="abs field" style="left:458px;top:163px;width:283px;height:47px">Phone Number</div>
  <div class="abs field" style="left:751px;top:163px;width:283px;height:47px">Email Address</div>
  <div class="abs field" style="left:165px;top:222px;width:869px;height:93px;line-height:20px;padding-top:14px">Message...!</div>
  <div class="abs send">SEND MESSAGE</div>
</section>

<footer class="abs footer">
  <div class="abs brand"><span class="sq"></span>Kestrel9 Recruitment</div>
  <div class="abs fcol" style="left:434px;top:72px;width:215px">
    <h4>Contact Us</h4>
    <div class="frow" style="margin-top:22px"><span class="ico"><svg width="14" height="16" viewBox="0 0 14 18"><path fill="#17b320" d="M7 0a7 7 0 0 0-7 7c0 5 7 11 7 11s7-6 7-11a7 7 0 0 0-7-7zm0 10a3 3 0 1 1 0-6 3 3 0 0 1 0 6z"/></svg></span><span>18 Quarry Lane,<br>Australia</span></div>
    <div class="frow"><span class="ico"><svg width="15" height="15" viewBox="0 0 24 24"><path fill="#17b320" d="M6.6 10.8a15 15 0 0 0 6.6 6.6l2.2-2.2c.3-.3.7-.4 1-.2 1.1.4 2.3.6 3.6.6.6 0 1 .4 1 1V20c0 .6-.4 1-1 1A17 17 0 0 1 3 4c0-.6.4-1 1-1h3.5c.6 0 1 .4 1 1 0 1.3.2 2.5.6 3.6.1.3 0 .7-.2 1z"/></svg></span><span style="white-space:nowrap">Call Us:<br>0400 555 921, +1 300 555 018</span></div>
    <div class="frow"><span class="ico"><svg width="15" height="12" viewBox="0 0 20 14"><rect x="1" y="1" width="18" height="12" fill="none" stroke="#17b320" stroke-width="2"/><path d="M1 1l9 7 9-7" fill="none" stroke="#17b320" stroke-width="2"/></svg></span><span style="white-space:nowrap">Email Us:<br>hello@kestrel9recruitment.com.au</span></div>
  </div>
  <div class="abs fcol" style="left:769px;top:72px;width:112px">
    <h4>Quick Links</h4>
    <ul class="links" style="margin-top:8px"><li>Home</li><li style="margin-top:18px">About Us</li><li style="margin-top:18px">Services</li><li style="margin-top:18px">Blog</li><li style="margin-top:18px">Contact us</li></ul>
  </div>
  <div class="abs fcol" style="left:949px;top:72px;width:140px">
    <h4>Follow Us</h4>
    <div class="frow" style="margin-top:22px"><span class="ico"><span style="width:10px;height:10px;background:var(--green);border-radius:50%"></span></span><span>Follow Us On<br>FEEDLINE</span></div>
    <div class="frow"><span class="ico"><span style="width:10px;height:10px;background:var(--green);border-radius:50%"></span></span><span>Follow Us On<br>SNAPFRAME</span></div>
    <div class="frow"><span class="ico"><span style="width:10px;height:10px;background:var(--green);border-radius:50%"></span></span><span>Follow Us On<br>CHIRPNET</span></div>
  </div>
  <div class="abs copy">Copyright © 2023 Kestrel9 recruitment pvt ltd - All Rights Reserved.</div>
</footer>

</body>
</html>
```